Heronby Mortgage Capital Business Card

We need a business card design for our mortgage servicing company. In addition to servicing the loans of homeowners, we help homeowners with purchasing their homes and any mortgage refinancing. We would like to see designs that use the colors in the logo attached below (gold-ish yellow and navy blue), and any other design you deem fit! The design should communicate a simpler life with smart mortgages provided by Heronby.

```html
<!DOCTYPE html>
<html lang="en">
<head>
<meta charset="utf-8">
<title>Heronby Mortgage Capital – Business Card</title>
<link href="https://fonts.googleapis.com/css2?family=Poppins:wght@400;600&display=swap" rel="stylesheet">
<style>
  :root {
    --khaki: #b3b17b;
    --navy: #00115a;
    --gold: #dfb13f;
    --white: #ffffff;
    --backdrop: #d6d6d6;
  }
  html, body {
    margin: 0;
    width: 1200px;
    height: 1200px;
    overflow: hidden;
    background: var(--backdrop);
    font-family: "Poppins", sans-serif;
  }
  .sheet {
    width: 1200px;
    height: 1200px;
    display: flex;
    align-items: center;
    justify-content: center;
    gap: 40px;
  }
  .card {
    position: relative;
    width: 540px;
    height: 310px;
    overflow: hidden;
  }
  .card-shapes {
    position: absolute;
    inset: 0;
    width: 100%;
    height: 100%;
    display: block;
  }
  .brand {
    position: absolute;
    display: flex;
    align-items: center;
    gap: 10px;
    color: var(--navy);
    font-weight: 600;
    line-height: 1;
  }
  .brand-dot {
    border-radius: 50%;
    background: var(--gold);
    flex: none;
  }
  .brand-name { display: flex; flex-direction: column; }
  .brand-word { letter-spacing: 0.5px; }
  .brand-sub { letter-spacing: 3px; margin-top: 4px; }

  .front .brand { left: 92px; top: 118px; }
  .front .brand-dot { width: 22px; height: 22px; }
  .front .brand-word { font-size: 48px; }
  .front .brand-sub { font-size: 14px; }

  .back .brand { left: 52px; top: 136px; gap: 7px; }
  .back .brand-dot { width: 12px; height: 12px; }
  .back .brand-word { font-size: 27px; }
  .back .brand-sub { font-size: 8px; letter-spacing: 2px; margin-top: 3px; }

  .contact-list {
    position: absolute;
    left: 298px;
    top: 88px;
    margin: 0;
    padding: 0;
    list-style: none;
    color: var(--white);
    font-size: 9px;
    font-weight: 400;
    letter-spacing: 2.6px;
    text-transform: uppercase;
  }
  .contact-item {
    display: flex;
    align-items: flex-start;
    gap: 14px;
    margin-bottom: 17px;
    line-height: 1.45;
  }
  .contact-icon { width: 14px; height: 14px; flex: none; margin-top: -1px; }
</style>
</head>
<body>
<main class="sheet">

  <section class="card front" aria-label="Card front">
    <svg class="card-shapes" viewBox="0 0 540 310" preserveAspectRatio="none" aria-hidden="true">
      <rect width="540" height="310" fill="var(--navy)"/>
      <polygon points="0,0 439,0 528,155 439,310 0,310" fill="var(--khaki)"/>
    </svg>
    <div class="brand">
      <span class="brand-dot"></span>
      <span class="brand-name">
        <span class="brand-word">Heronby</span>
        <span class="brand-sub">MORTGAGE</span>
      </span>
    </div>
  </section>

  <section class="card back" aria-label="Card back">
    <svg class="card-shapes" viewBox="0 0 540 310" preserveAspectRatio="none" aria-hidden="true">
      <rect width="540" height="310" fill="var(--navy)"/>
      <polygon points="0,0 165,0 140,45 140,265 165,310 0,310" fill="var(--gold)"/>
      <polygon points="89,45 216,45 278,155 216,265 89,265 26,155" fill="var(--khaki)"/>
    </svg>
    <div class="brand">
      <span class="brand-dot"></span>
      <span class="brand-name">
        <span class="brand-word">Heronby</span>
        <span class="brand-sub">MORTGAGE</span>
      </span>
    </div>
    <ul class="contact-list">
      <li class="contact-item">
        <svg class="contact-icon" viewBox="0 0 24 24" aria-hidden="true"><path fill="#fff" d="M17 2l3 3-3 4-2-1-5 8 2 2-2 4-3-1C6 17 10 7 15 3z"/></svg>
        <span>+00-0000-0000-000</span>
      </li>
      <li class="contact-item">
        <svg class="contact-icon" viewBox="0 0 24 24" aria-hidden="true"><rect x="2" y="5" width="20" height="14" fill="none" stroke="#fff" stroke-width="2"/><path d="M2 5l10 8 10-8" fill="none" stroke="#fff" stroke-width="2"/></svg>
        <span>info@companyname.com</span>
      </li>
      <li class="contact-item">
        <svg class="contact-icon" viewBox="0 0 24 24" aria-hidden="true"><g fill="none" stroke="#fff" stroke-width="2"><circle cx="12" cy="12" r="10"/><ellipse cx="12" cy="12" rx="4" ry="10"/><path d="M2 12h20M4 7h16M4 17h16"/></g></svg>
        <span>www.companyname.com</span>
      </li>
      <li class="contact-item">
        <svg class="contact-icon" viewBox="0 0 24 24" aria-hidden="true"><path fill="#fff" d="M12 1a7 7 0 0 0-7 7c0 5 7 15 7 15s7-10 7-15a7 7 0 0 0-7-7zm0 10a3 3 0 1 1 0-6 3 3 0 0 1 0 6z"/></svg>
        <span>1234 your location here<br>your rd. your street<br>postal 00000</span>
      </li>
    </ul>
  </section>

</main>
</body>
</html>
```